Home Remodeler Needs a Website!

Single page (plus contact form) website for small home remodeling company. He's got a few pictures he'd like on the site and needs some basic text. He likes clean, simple designs and is "more traditional" in his stylistic preferences. Most of his business comes from word-of-mouth advertising and so the site is just something he needs for people to feel more comfortable with his business.

Target Market(s)

People who want to remodel their homes

Coding

Coded - Design and coding required

Number of Pages Required

2 page

Requirements
Must have
• Main page to include some or all of the attached images, contact page. Neutral colors. Old domain: brindlecoveabodes.com New domain: qm-holdings.com You can pull text from the old site or update it.
Should not have
• No loud colors/loud visual elements

```html
<!DOCTYPE html>
<html lang="en">
<head>
<meta charset="utf-8">
<title>Brindle Cove Abodes</title>
<link rel="stylesheet" href="https://fonts.googleapis.com/css2?family=Montserrat:wght@400;500;700&family=Playfair+Display:ital,wght@1,400;1,700&display=swap">
<style>
:root{
  --forest:#0e4634;
  --forest-deep:#0a3a2b;
  --sage:#c9dec3;
  --sage-dark:#a9c7a3;
  --white:#ffffff;
  --ink:#333a36;
  --grey-hex:#d9dcda;
}
*{box-sizing:border-box;margin:0;padding:0}
html,body{width:1200px;height:2400px;overflow:hidden}
body{position:relative;background:var(--white);font-family:'Montserrat',sans-serif;color:var(--ink)}
.abs{position:absolute}
.script{font-family:'Playfair Display',serif;font-style:italic;font-weight:700;text-transform:uppercase;line-height:1.05}

/* header */
.site-header{left:0;top:0;width:1200px;height:44px;background:var(--forest);display:flex;align-items:center;justify-content:space-between;padding:0 140px 0 260px;color:var(--white)}
.brand{font-weight:700;font-size:15px;letter-spacing:.5px}
.nav{display:flex;gap:22px;font-size:11px;font-weight:700;letter-spacing:.5px}

/* hero */
.hero{left:0;top:44px;width:1200px;height:460px;background:var(--sage)}
.hero-pattern{left:0;top:70px;width:250px;height:240px;background:linear-gradient(135deg,#b8d1b2,#c9dec3)}
.hero-photo{left:272px;top:150px;width:290px;height:270px;background:linear-gradient(160deg,#6d5a47,#2e2b2a 60%,#8c7864)}
.hero-title{left:730px;top:96px;width:330px;text-align:right;font-size:40px;color:var(--forest)}
.hero-tag{left:760px;top:306px;width:300px;font-size:15px;line-height:1.45;color:var(--ink);text-transform:uppercase}
.hero-tag b{color:var(--forest-deep)}

/* about */
.about-title{left:264px;top:552px;font-size:34px;color:var(--forest)}
.about-title .lead{font-weight:400}
.about-copy{left:264px;top:650px;width:560px;font-size:10.5px;line-height:1.5}
.about-copy p{margin-bottom:10px}
.about-copy .caps{font-weight:700;text-transform:uppercase}
.about-pattern{left:960px;top:420px;width:240px;height:480px}

/* feature band */
.feature{left:0;top:928px;width:1200px;height:342px;background:var(--forest)}
.feature-photo{left:262px;top:980px;width:320px;height:250px;background:linear-gradient(180deg,#e8e4dc,#a59684 55%,#3e3128)}
.feature-copy{left:610px;top:984px;width:300px;color:var(--white);font-size:13px;line-height:1.5}
.feature-copy p{margin-bottom:14px}

/* services */
.services-title{left:270px;top:1326px;font-size:32px;color:var(--forest)}
.services-title .lead{font-weight:400}
.services-pattern{left:0;top:1400px;width:230px;height:230px;background:linear-gradient(90deg,#e3e5e4,#f4f5f4)}
.service{width:160px;text-align:center;font-size:13px;font-weight:500}
.service svg{display:block;margin:0 auto 10px}

/* contact */
.contact{left:0;top:1748px;width:1200px;height:372px;background:var(--forest)}
.contact-title{left:270px;top:1786px;font-size:30px;color:var(--white)}
.contact-title .lead{font-weight:400}
.field{height:26px;border:1px solid #7fa190;color:#cfe0d6;font-size:10px;padding:7px 8px}
.submit{left:262px;top:2078px;width:64px;height:22px;background:var(--white);color:var(--forest);font-size:10px;font-weight:700;text-align:center;line-height:22px}
.contact-photo{left:600px;top:1748px;width:600px;height:372px;background:linear-gradient(150deg,#2a1d15,#6b4a2e 45%,#1b1714)}

/* footer */
.site-footer{left:0;top:2120px;width:1200px;height:280px;background:var(--sage)}
.foot-col{top:2180px;width:220px;text-align:center;font-size:11px;line-height:1.6}
.foot-col h4{font-family:'Playfair Display',serif;font-style:italic;font-weight:700;font-size:15px;color:var(--forest);margin:10px 0 6px}
.copyright{left:0;top:2372px;width:1200px;text-align:center;font-size:10px;color:var(--ink)}
</style>
</head>
<body>

<header class="abs site-header">
  <div class="brand">BRINDLE COVE ABODES</div>
  <nav class="nav"><span>HOME</span><span>ABOUT</span><span>SERVICES</span><span>CONTACT</span></nav>
</header>

<section class="abs hero"></section>
<div class="abs hero-pattern" role="img" aria-label="Decorative hexagon pattern in soft sage tones"></div>
<div class="abs hero-photo" role="img" aria-label="Photo of a remodeled kitchen with stainless appliances"></div>
<h1 class="abs script hero-title">Welcome to<br>Brindle Cove<br>Abodes</h1>
<p class="abs hero-tag">When you want <b>affordable, quality</b> home construction services <b>think of us to do the job.</b></p>

<h2 class="abs script about-title"><span class="lead">About</span><br>Brindle Cove Abodes</h2>
<div class="abs about-pattern" role="img" aria-label="Decorative dark green hexagon pattern">
  <svg width="240" height="480" viewBox="0 0 240 480"><path d="M240 0 V480 L120 400 L60 200 Z" fill="#ffffff"/><polygon points="60,40 240,40 240,300 120,330 40,200" fill="var(--forest)" opacity=".92"/></svg>
</div>
<div class="abs about-copy">
  <p>Since 1993 our team has built and remodeled homes with honest work and fair prices. We treat your home as if it were our own and finish every job.</p>
  <p>We offer quality, value and personal attention to detail you can count on.</p>
  <p>With over 25 years of experience in residential and commercial construction, you can trust your project to Brindle Cove Abodes.</p>
  <p class="caps">"Don't Trade Around"</p>
  <p>Our crew built this business through lasting partnerships with local suppliers, trades and designers. Every project is shaped by careful planning, steady communication and clean work.</p>
  <p>These days "trade for trade" is a rare value, but it remains at the heart of how we run our company.</p>
  <p>We use the best materials and the most skilled trades to deliver a finished home you will love.</p>
  <p>Our personal touch and our friendly service set us apart from the rest. When called upon to improve their own homes, our clients come back to us again and again.</p>
</div>

<section class="abs feature"></section>
<div class="abs feature-photo" role="img" aria-label="Photo of a finished basement with polished floor"></div>
<div class="abs feature-copy">
  <p>When you love your home as your castle, you appreciate craftsmen working on it with a sense of respect.</p>
  <p>"When the light goes on for a better idea we want to be there to enjoy it too!"</p>
  <p>Since Brindle Cove Abodes is in Middle Tennessee, we are constantly working with time-proven architectural ideas, as well as new influences that come to our area from other parts of the country.</p>
</div>

<div class="abs services-pattern" role="img" aria-label="Decorative light grey hexagon pattern"></div>
<h2 class="abs script services-title"><span class="lead">Our</span><br>Services</h2>

<div class="abs service" style="left:228px;top:1440px"><svg width="62" height="62" viewBox="0 0 62 62"><rect x="12" y="12" width="38" height="38" transform="rotate(45 31 31)" fill="var(--forest)"/><path d="M20 32 L31 22 L42 32 M24 30 V40 H38 V30" stroke="#fff" stroke-width="2.5" fill="none"/></svg>Roofing</div>
<div class="abs service" style="left:400px;top:1440px"><svg width="62" height="62" viewBox="0 0 62 62"><rect x="12" y="12" width="38" height="38" transform="rotate(45 31 31)" fill="var(--forest)"/><rect x="23" y="23" width="16" height="16" stroke="#fff" stroke-width="2.5" fill="none"/><path d="M31 23 V39 M23 31 H39" stroke="#fff" stroke-width="2"/></svg>Window Replacement</div>
<div class="abs service" style="left:616px;top:1440px"><svg width="62" height="62" viewBox="0 0 62 62"><rect x="12" y="12" width="38" height="38" transform="rotate(45 31 31)" fill="var(--forest)"/><path d="M33 20 L25 33 H31 L28 42 L37 28 H31 Z" fill="#fff"/></svg>Electrical</div>
<div class="abs service" style="left:808px;top:1440px"><svg width="62" height="62" viewBox="0 0 62 62"><rect x="12" y="12" width="38" height="38" transform="rotate(45 31 31)" fill="var(--forest)"/><path d="M31 21 V41 M22 26 L40 36 M22 36 L40 26" stroke="#fff" stroke-width="2.5"/></svg>Air Conditioning</div>

<div class="abs service" style="left:228px;top:1604px"><svg width="62" height="62" viewBox="0 0 62 62"><rect x="12" y="12" width="38" height="38" transform="rotate(45 31 31)" fill="var(--forest)"/><path d="M22 26 H34 V38 M30 38 H38" stroke="#fff" stroke-width="3" fill="none"/></svg>Plumbing Upgrades</div>
<div class="abs service" style="left:400px;top:1604px"><svg width="62" height="62" viewBox="0 0 62 62"><rect x="12" y="12" width="38" height="38" transform="rotate(45 31 31)" fill="var(--forest)"/><rect x="22" y="23" width="18" height="7" fill="#fff"/><path d="M31 30 V40" stroke="#fff" stroke-width="3"/></svg>Painting</div>
<div class="abs service" style="left:616px;top:1604px"><svg width="62" height="62" viewBox="0 0 62 62"><rect x="12" y="12" width="38" height="38" transform="rotate(45 31 31)" fill="var(--forest)"/><path d="M21 25 H41 V30 H21 Z M36 30 V40" stroke="#fff" stroke-width="2.5" fill="none"/></svg>Gutters</div>
<div class="abs service" style="left:808px;top:1604px"><svg width="62" height="62" viewBox="0 0 62 62"><rect x="12" y="12" width="38" height="38" transform="rotate(45 31 31)" fill="var(--forest)"/><path d="M21 36 H41 M23 30 H39 M26 24 H36" stroke="#fff" stroke-width="3"/></svg>Concrete Work</div>

<section class="abs contact"></section>
<h2 class="abs script contact-title"><span class="lead">Contact</span> Brindle<br>Cove Abodes</h2>
<div class="abs field" style="left:262px;top:1878px;width:148px">First Name</div>
<div class="abs field" style="left:420px;top:1878px;width:148px">Last Name</div>
<div class="abs field" style="left:262px;top:1914px;width:148px">Email</div>
<div class="abs field" style="left:420px;top:1914px;width:148px">Phone</div>
<div class="abs field" style="left:262px;top:1950px;width:306px;height:108px">Message</div>
<div class="abs submit">SUBMIT</div>
<div class="abs contact-photo" role="img" aria-label="Photo of a dark wood kitchen with island and bar stools"></div>

<footer class="abs site-footer"></footer>
<div class="abs foot-col" style="left:180px">
  <svg width="28" height="28" viewBox="0 0 24 24"><path d="M6.6 10.8a15 15 0 0 0 6.6 6.6l2.2-2.2c.3-.3.7-.4 1-.2 1.1.4 2.3.6 3.6.6.6 0 1 .4 1 1V20c0 .6-.4 1-1 1A17 17 0 0 1 3 4c0-.6.4-1 1-1h3.5c.6 0 1 .4 1 1 0 1.3.2 2.5.6 3.6.1.3 0 .7-.2 1z" fill="var(--ink)"/></svg>
  <h4>PHONE</h4>
  <div>(615) 555-0142</div><div>(615) 555-0187</div>
</div>
<div class="abs foot-col" style="left:490px">
  <svg width="28" height="28" viewBox="0 0 24 24"><rect x="2" y="5" width="20" height="14" fill="var(--ink)"/><path d="M2 5 L12 13 L22 5" stroke="#c9dec3" stroke-width="1.6" fill="none"/></svg>
  <h4>EMAIL</h4>
  <div>info@brindlecoveabodes.com</div>
</div>
<div class="abs foot-col" style="left:800px">
  <svg width="28" height="28" viewBox="0 0 24 24"><path d="M2 10 H6 V21 H2 Z M8 21 V10 L13 3 C15 3 15 5 14.5 7 L14 9 H20 C21.5 9 22 10.5 21.5 12 L19 20 C18.7 20.7 18 21 17 21 Z" fill="var(--ink)"/></svg>
  <h4>FOLLOW US</h4>
  <svg width="70" height="22" viewBox="0 0 70 22"><rect x="4" y="4" width="14" height="14" transform="rotate(45 11 11)" fill="var(--forest)"/><rect x="28" y="4" width="14" height="14" transform="rotate(45 35 11)" fill="var(--forest)"/><rect x="52" y="4" width="14" height="14" transform="rotate(45 59 11)" fill="var(--forest)"/></svg>
</div>
<p class="abs copyright">Copyright © 2024 Brindle Cove Abodes. All rights reserved.</p>

</body>
</html>
```